Design a One Pager - About vTa

We are looking to produce a one pager that introduces our brand vTa in a nutshell (see www.vta.co.uk)
This should be on one page (not the back) and respect the vTa branding.
We have produced a one pager previously (here attached) but want to review the general design of it (in particular the graphs) and the content.
The new content is attached.
The first paragraph in the content file needs to be first.
Then there will be a title for the graph: Your Cloud Delivery Partner
We need a graph below that will be a mix of the one on the pager and of the green one attached. I have mocked up a draft version to show how it should look like in terms of placement / content.
This graph will show the following:
- entities on the left: head office / branch office / mobile working / home office / data centre. They all link to in the middle an entity with vTa: Network (preferably with the vTa logo) in the middle and below 'Enterprise WAN'
- Then below a link to another entity called Public internet.
- Then on the right 4 links to 4 different entities - one called Public Cloud (with logo nimbra data works / Quellon Skyview in it) / one called Private Cloud (with logo Tessvia in it) / one called SaaS / one called Cloud Telephony.
Below the graph there should be a list of bullet points about vTa (see content attached).
At the bottom there should be contact details (as seen on the original one pager) plus enough room to add some of our customers logos.
The colours of our brand are Pantone 432 / Pantone 549 but we're happy to introduce new colours in the mix (we sometimes use an orange - see website www.vta.co.uk) if they fit with the branding.
We have found some examples of one pagers that we like in style and because they don’t look too crowded.
https://uk.boardpinly.com/pin/582017364920184477/
http://morvadelacroix.com/?portfolio=bold-service-offerings-one-pager-draft-in-progress
https://www.deckvault.net/halvardmoensink/zepora-flyer-for-ktx-2013
Thank you

```html
<!DOCTYPE html>
<html lang="en">
<head>
<meta charset="utf-8">
<title>vTa – One Pager</title>
<link rel="stylesheet" href="https://fonts.googleapis.com/css2?family=Lato:wght@300;400;700&family=Oswald:wght@300;400&display=swap">
<style>
  :root{
    --backdrop:#8a8a8a;
    --paper:#ffffff;
    --brand-blue:#4f97c2;
    --sky:#62aedb;
    --ink:#2a2a2a;
    --muted:#555;
    --diagram-bg:#d9d9db;
    --hub-ring:#2f2f2f;
    --footer:#565656;
    --hero-a:#2c3a4c;
    --hero-b:#5b6f86;
  }
  *{margin:0;padding:0;box-sizing:border-box}
  html,body{width:1200px;height:1200px;overflow:hidden;background:var(--backdrop)}
  body{font-family:"Lato",sans-serif;color:var(--ink)}
  .page{position:absolute;left:171px;top:0;width:857px;height:1200px;background:var(--paper);overflow:hidden}
  .hero{position:absolute;left:0;top:0;width:857px;height:215px;
    background:linear-gradient(160deg,var(--hero-a) 0%,var(--hero-b) 45%,#3b4b60 75%,#1f2b3a 100%)}
  .hero-frame{position:absolute;left:21px;top:52px;width:800px;height:133px;border:1px solid var(--sky);
    display:flex;align-items:center;justify-content:center}
  .hero-title{font-family:"Oswald",sans-serif;font-weight:300;font-size:54px;color:#fff;letter-spacing:1px;line-height:1;white-space:nowrap}
  .brand-row{position:absolute;left:0;top:215px;width:857px;height:92px}
  .brand-name{position:absolute;left:56px;top:14px;font-size:60px;font-weight:400;color:#3a3a3a;line-height:1}
  .contact-phone,.contact-web{position:absolute;top:36px;font-size:27px;font-weight:400;color:var(--brand-blue);line-height:1}
  .contact-phone{left:330px}
  .contact-web{left:593px}
  .icon-phone{position:absolute;left:292px;top:40px}
  .icon-globe{position:absolute;left:551px;top:40px}
  .row-divider{position:absolute;left:537px;top:37px;width:1px;height:30px;background:#555}
  .rule{position:absolute;left:0;width:857px;height:3px;background:var(--sky)}
  .about{position:absolute;left:56px;top:322px;width:760px}
  .about h2{font-size:19px;font-weight:400;color:var(--brand-blue);margin-bottom:6px}
  .about p{font-size:12.3px;line-height:15px;margin-bottom:4.5px;color:var(--ink)}
  .diagram{position:absolute;left:0;top:502px;width:857px;height:370px;background:var(--diagram-bg)}
  .logos-space{position:absolute;left:0;top:876px;width:857px;height:111px;display:flex;align-items:center;justify-content:center}
  .logos-space span{font-size:44px;color:var(--brand-blue);font-weight:400;letter-spacing:.5px}
  .facts{position:absolute;top:1018px;list-style:none;font-size:12.5px;color:var(--muted)}
  .facts li{position:relative;padding-left:17px;height:21px;line-height:15px}
  .facts li::before{content:"";position:absolute;left:0;top:3px;width:7px;height:7px;border:2px solid var(--brand-blue);border-radius:50%}
  .facts li.plain::before{display:none}
  .facts li.strong{font-weight:700;color:#555}
  .facts li.two-line{height:36px}
  .facts-a{left:77px}.facts-b{left:320px}.facts-c{left:575px}
  .col-divider{position:absolute;top:1020px;width:1px;height:74px;background:var(--brand-blue)}
  .partners{position:absolute;left:323px;top:1094px;display:flex;gap:14px;font-size:11px;font-weight:700;color:#333}
  .footer{position:absolute;left:0;top:1128px;width:857px;height:72px;background:var(--footer);color:#fff;font-size:14.5px}
  .footer .f-item{position:absolute;top:27px;line-height:1}
  .footer .f-div{position:absolute;top:22px;width:2px;height:30px;background:#fff}
  .footer svg{position:absolute}
  .f-address{top:20px!important;line-height:17px!important}
  .node rect{fill:#fff;stroke:var(--brand-blue);stroke-width:2.5}
  .node text{font-size:12px;fill:#333;text-anchor:middle}
</style>
</head>
<body>
<main class="page">
  <header class="hero" role="img" aria-label="Photo of a business person holding a tablet over a night city skyline with network lines">
    <div class="hero-frame"><h1 class="hero-title">YOUR CLOUD DELIVERY PARTNER</h1></div>
  </header>

  <section class="brand-row">
    <div class="brand-name">vTa</div>
    <svg class="icon-phone" width="26" height="26" viewBox="0 0 26 26"><circle cx="13" cy="13" r="11.5" fill="none" stroke="#4f97c2" stroke-width="2"/><path d="M9 7c1 0 2 2 2 3s-1 1-1 2 2 4 4 4 1-1 2-1 3 1 3 2-1 2-3 2c-4 0-9-5-9-9 0-2 1-3 2-3z" fill="none" stroke="#4f97c2" stroke-width="1.6"/></svg>
    <span class="contact-phone">020 7915 3362</span>
    <div class="row-divider"></div>
    <svg class="icon-globe" width="26" height="26" viewBox="0 0 26 26" fill="none" stroke="#4f97c2" stroke-width="1.6"><circle cx="13" cy="13" r="11.5"/><ellipse cx="13" cy="13" rx="5" ry="11.5"/><path d="M2 13h22M4 7h18M4 19h18"/></svg>
    <span class="contact-web">www.vta.co.uk</span>
  </section>
  <div class="rule" style="top:307px"></div>

  <section class="about">
    <h2>About vTa</h2>
    <p>vTa is a leading and award winning network service provider specialising in delivering cloud solutions for voice, data and IT security.</p>
    <p>Our network, communications and computing platforms, combined with our committed service, will let your business applications run more smoothly, securely and continuously.</p>
    <p>We provide UK organisations with whole of market site-to-site connectivity, Internet access, hosted telephony, virtualisation and direct connections to public clouds.</p>
    <p>We tailor our services to create a solution to meet your business requirements and budget.</p>
    <p>Our UK-based Network Operations Centre proactively monitors your services 24/7/365.</p>
  </section>

  <section class="diagram" aria-label="Network diagram">
    <svg width="857" height="370" viewBox="0 0 857 370" font-family="Lato, sans-serif">
      <g stroke="#333" stroke-width="1" stroke-dasharray="2 2" fill="none">
        <line x1="429" y1="175" x2="200" y2="55"/><line x1="429" y1="175" x2="160" y2="115"/>
        <line x1="429" y1="175" x2="140" y2="182"/><line x1="429" y1="175" x2="150" y2="255"/>
        <line x1="429" y1="175" x2="195" y2="320"/><line x1="429" y1="175" x2="429" y2="325"/>
        <line x1="429" y1="175" x2="640" y2="45"/><line x1="429" y1="175" x2="690" y2="115"/>
        <line x1="429" y1="175" x2="700" y2="194"/><line x1="429" y1="175" x2="670" y2="280"/>
      </g>
      <circle cx="429" cy="175" r="86" fill="#fff" stroke="var(--brand-blue)" stroke-width="6"/>
      <text x="429" y="148" font-size="22" fill="#3a3a3a" text-anchor="middle">vTa</text>
      <text x="429" y="181" font-size="20" fill="#333" text-anchor="middle">Network</text>
      <text x="429" y="205" font-size="18.5" fill="#222" text-anchor="middle">Enterprise WAN</text>

      <g class="node"><rect x="150" y="40" width="100" height="30" rx="15"/><text x="200" y="59">Head Office</text></g>
      <g class="node"><rect x="110" y="100" width="100" height="30" rx="15"/><text x="160" y="119">Home Office</text></g>
      <g class="node"><rect x="90" y="167" width="100" height="30" rx="15"/><text x="140" y="186">Branch Office</text></g>
      <g class="node"><rect x="100" y="240" width="100" height="30" rx="15"/><text x="150" y="259">Mobile working</text></g>
      <g class="node"><rect x="145" y="305" width="100" height="30" rx="15"/><text x="195" y="324">Data Centre</text></g>
      <g class="node"><rect x="374" y="312" width="110" height="30" rx="15"/><text x="429" y="331">Public Internet</text></g>

      <g class="node"><rect x="585" y="22" width="110" height="46" rx="14"/><text x="640" y="41" style="fill:var(--brand-blue)">Private Cloud</text><text x="640" y="58">Tessvia</text></g>
      <g class="node"><rect x="625" y="92" width="130" height="46" rx="14"/><text x="690" y="111">Quellon Skyview</text><text x="690" y="128">nimbra data works</text></g>
      <g class="node"><rect x="660" y="179" width="80" height="30" rx="15"/><text x="700" y="198" style="fill:var(--brand-blue)">SaaS</text></g>
      <g class="node"><rect x="610" y="265" width="120" height="30" rx="15"/><text x="670" y="284">Cloud Telephony</text></g>
    </svg>
  </section>
  <div class="rule" style="top:872px"></div>

  <section class="logos-space"><span>SPACE FOR&nbsp; BRAND LOGOS</span></section>
  <div class="rule" style="top:987px"></div>

  <ul class="facts facts-a">
    <li>Carrier-independent connectivity</li>
    <li>End-to-end converged networks</li>
    <li>UK-based proactive monitoring</li>
    <li class="plain">30+ points of presence</li>
  </ul>
  <div class="col-divider" style="left:297px"></div>
  <ul class="facts facts-b">
    <li>ISO 9001 / ISO 27001 / ISO 20000</li>
    <li>Over 15 years of service</li>
    <li class="strong">Public and Private cloud expertise</li>
  </ul>
  <div class="partners"><span>Tessvia</span><span>Quellon Skyview</span><span>nimbra data works</span></div>
  <div class="col-divider" style="left:552px"></div>
  <ul class="facts facts-c">
    <li class="two-line">Choice of security technologies<br>(DDoS, Firewalls, VPNs)</li>
    <li>24/7 NOC</li>
    <li>Over 500 customers</li>
  </ul>

  <footer class="footer">
    <svg style="left:58px;top:16px" width="32" height="32" viewBox="0 0 32 32" fill="var(--sky)"><circle cx="16" cy="9" r="8"/><path d="M1 32c0-9 7-13 15-13s15 4 15 13z"/></svg>
    <span class="f-item" style="left:110px">sales man name</span>
    <div class="f-div" style="left:240px"></div>
    <svg style="left:256px;top:24px" width="24" height="24" viewBox="0 0 26 26"><circle cx="13" cy="13" r="11.5" fill="none" stroke="#62aedb" stroke-width="2"/><path d="M9 7c1 0 2 2 2 3s-1 1-1 2 2 4 4 4 1-1 2-1 3 1 3 2-1 2-3 2c-4 0-9-5-9-9 0-2 1-3 2-3z" fill="none" stroke="#62aedb" stroke-width="1.6"/></svg>
    <span class="f-item" style="left:288px;font-weight:700">07712 460 538</span>
    <div class="f-div" style="left:432px"></div>
    <svg style="left:456px;top:28px" width="24" height="18" viewBox="0 0 24 18" fill="none" stroke="#62aedb" stroke-width="2"><rect x="1" y="1" width="22" height="16"/><path d="M1 1l11 9 11-9"/></svg>
    <span class="f-item" style="left:490px;font-weight:700">info@vta.co.uk</span>
    <div class="f-div" style="left:628px"></div>
    <svg style="left:643px;top:24px" width="22" height="28" viewBox="0 0 22 28"><path d="M11 27C4 18 1 14 1 10a10 10 0 0 1 20 0c0 4-3 8-10 17z" fill="#62aedb"/><circle cx="11" cy="10" r="4" fill="#565656"/></svg>
    <span class="f-item f-address" style="left:674px">vTa 18 Carrow Lane,<br>London E2 7QT</span>
  </footer>
</main>
</body>
</html>
```